Coin collector banner ad for specialty insurance

We need a logo designed banner ad (multiple ads) to align with the coin collector market while incorporating color palette logo and call to action. Color palette of Kestrelby. Dimension, images, example designs and color palette attached. The context should include 'Specialty Insurance for your coin collection' please refer to the designed examples

Target Market(s)

Coin collectors 30-65+ years of age primarily male

Industry/Entity Type

Insurance

Font styles to use
Sans Serif

Requirements
Must have
• color palette, logo, word mark, Call to Action, The words 'Specialty Insurance for your coin collection'
Nice to have
• Call to actions
Should not have
• ba

```html
<!DOCTYPE html>
<html lang="en">
<head>
<meta charset="utf-8">
<title>Kestrelby coin collection insurance banners</title>
<link href="https://fonts.googleapis.com/css2?family=Open+Sans:wght@400;600;700;800&display=swap" rel="stylesheet">
<style>
  :root{
    --canvas:#a7a8ab;
    --brand-blue:#0aa3dc;
    --white:#ffffff;
    --ink:#1d1d1f;
    --label:#1a1a1a;
    --copper:#a8623f;
    --silver:#d6d7da;
    --gold:#c9a43c;
    --dark:#2a2a2a;
  }
  *{margin:0;padding:0;box-sizing:border-box}
  html,body{width:1043px;height:1200px;overflow:hidden}
  body{background:var(--canvas);font-family:"Open Sans",Arial,sans-serif;position:relative}
  .size-label{position:absolute;font-size:10px;font-weight:600;color:var(--label);letter-spacing:.2px}
  .banner{position:absolute;background:var(--white);overflow:hidden}
  .banner svg.shapes{position:absolute;left:0;top:0}
  .coins{position:absolute;top:0;height:100%}
  .coins-mix{background:linear-gradient(90deg,var(--copper) 0%,#c98a66 18%,var(--silver) 38%,#f2f2f3 50%,var(--dark) 60%,var(--gold) 75%,#a8862c 100%)}
  .coins-trio{background:radial-gradient(circle at 30% 75%,#c89a4a 0 18%,transparent 19%),radial-gradient(circle at 52% 80%,#c7c6c0 0 24%,transparent 25%),radial-gradient(circle at 85% 15%,var(--copper) 0 22%,transparent 23%),radial-gradient(circle at 80% 70%,var(--gold) 0 34%,transparent 35%),linear-gradient(90deg,var(--white) 0%,var(--silver) 40%,#e8e8ea 60%,var(--gold) 100%)}
  .coins-duo{background:radial-gradient(circle at 30% 55%,var(--silver) 0 42%,transparent 43%),radial-gradient(circle at 68% 50%,var(--gold) 0 55%,transparent 56%),var(--white)}
  .coin-round{position:absolute;border-radius:50%;background:radial-gradient(circle at 40% 40%,#f4f4f5,var(--silver) 55%,#8d8e92)}
  .headline{position:absolute;color:var(--white);text-align:center;line-height:1.08;text-transform:uppercase;white-space:nowrap}
  .headline .title{display:block;font-weight:800;letter-spacing:.3px}
  .headline .sub{display:block;font-weight:600;letter-spacing:.3px}
  .cta{position:absolute;background:var(--brand-blue);color:var(--white);font-weight:400;display:flex;align-items:center;justify-content:center;text-transform:uppercase;letter-spacing:.3px}
  .presented{position:absolute;font-size:6px;font-weight:800;color:var(--ink);text-transform:uppercase;letter-spacing:.3px}
  .wordmark{position:absolute;display:flex;align-items:center;gap:4px;color:var(--ink);font-weight:700;text-transform:uppercase;letter-spacing:-.2px;white-space:nowrap}
  .wordmark .mark{background:var(--brand-blue);display:block;flex:none}
</style>
</head>
<body>

<!-- 728x100 -->
<div class="size-label" style="left:74px;top:50px">728X100</div>
<div class="banner" style="left:72px;top:68px;width:468px;height:64px">
  <div class="coins coins-mix" role="img" aria-label="Row of overlapping copper, silver and gold coins" style="left:205px;width:175px"></div>
  <svg class="shapes" width="468" height="64" viewBox="0 0 468 64">
    <polygon points="0,0 208,0 216,32 208,64 0,64" fill="var(--brand-blue)"/>
    <polygon points="3,3 205,3 212,32 205,61 3,61" fill="none" stroke="var(--white)" stroke-width="1"/>
    <polygon points="374,0 468,0 468,64 374,64 366,32" fill="var(--white)"/>
    <polygon points="377,3 465,3 465,61 377,61 370,32" fill="none" stroke="var(--brand-blue)" stroke-width="1"/>
  </svg>
  <div class="headline" style="left:10px;top:18px;width:190px">
    <span class="title" style="font-size:13.5px">Specialty Insurance</span>
    <span class="sub" style="font-size:10.5px">For your coin collection</span>
  </div>
  <div class="presented" style="left:402px;top:20px;font-size:5px">Presented by</div>
  <div class="wordmark" style="left:383px;top:27px;font-size:10px"><span class="mark" style="width:11px;height:11px"></span>Kestrelby</div>
</div>

<!-- 930x255 -->
<div class="size-label" style="left:74px;top:150px">930X255</div>
<div class="banner" style="left:72px;top:167px;width:598px;height:163px">
  <div class="coins coins-duo" role="img" aria-label="Silver coin partly behind a large gold coin" style="left:365px;width:233px"></div>
  <svg class="shapes" width="400" height="90" viewBox="0 0 400 90">
    <path d="M0 0 H387 L356 60 Q341 87 308 87 H0 Z" fill="var(--brand-blue)"/>
    <path d="M4 4 H380 L352 57 Q338 83 308 83 H4 Z" fill="none" stroke="var(--white)" stroke-width="1.2"/>
  </svg>
  <div class="headline" style="left:10px;top:20px;width:320px">
    <span class="title" style="font-size:23px">Specialty Insurance</span>
    <span class="sub" style="font-size:17.5px">For your coin collection</span>
  </div>
  <div class="cta" style="left:17px;top:112px;width:121px;height:31px;font-size:12px">Learn more</div>
  <div class="presented" style="left:169px;top:131px;font-size:5.5px">Presented by</div>
  <div class="wordmark" style="left:218px;top:117px;font-size:15px"><span class="mark" style="width:21px;height:21px"></span>Kestrelby</div>
</div>

<!-- 880x340 -->
<div class="size-label" style="left:74px;top:372px">880X340</div>
<div class="banner" style="left:72px;top:394px;width:565px;height:218px">
  <div class="coins coins-trio" role="img" aria-label="Cluster of gold, silver and copper coins" style="left:190px;width:375px"></div>
  <svg class="shapes" width="400" height="115" viewBox="0 0 400 115">
    <path d="M0 0 H394 L366 78 Q352 110 318 110 H0 Z" fill="var(--brand-blue)"/>
    <path d="M4 4 H387 L362 75 Q349 106 318 106 H4 Z" fill="none" stroke="var(--white)" stroke-width="1.2"/>
  </svg>
  <div class="headline" style="left:10px;top:34px;width:320px">
    <span class="title" style="font-size:23px">Specialty Insurance</span>
    <span class="sub" style="font-size:17.5px">For your coin collection</span>
  </div>
  <div class="presented" style="left:46px;top:122px;font-size:5.5px">Presented by</div>
  <div class="wordmark" style="left:20px;top:129px;font-size:15px"><span class="mark" style="width:21px;height:21px"></span>Kestrelby</div>
  <div class="cta" style="left:14px;top:162px;width:157px;height:41px;font-size:15px">Learn more</div>
</div>

<!-- 490x285 -->
<div class="size-label" style="left:674px;top:412px">490X285</div>
<div class="banner" style="left:674px;top:428px;width:315px;height:184px">
  <div class="coins coins-trio" role="img" aria-label="Cluster of silver, copper and gold coins" style="left:140px;width:175px"></div>
  <svg class="shapes" width="250" height="95" viewBox="0 0 250 95">
    <path d="M0 0 H246 L222 64 Q212 91 188 91 H0 Z" fill="var(--brand-blue)"/>
    <path d="M4 4 H240 L218 62 Q209 87 188 87 H4 Z" fill="none" stroke="var(--white)" stroke-width="1"/>
  </svg>
  <div class="headline" style="left:12px;top:26px;width:200px">
    <span class="title" style="font-size:15.5px">Specialty Insurance</span>
    <span class="sub" style="font-size:12px">For your coin collection</span>
  </div>
  <div class="wordmark" style="left:12px;top:112px;font-size:10.5px"><span class="mark" style="width:15px;height:15px"></span>Kestrelby</div>
  <div class="cta" style="left:9px;top:142px;width:113px;height:29px;font-size:11px">Learn more</div>
</div>

<!-- 980x200 -->
<div class="size-label" style="left:72px;top:664px">980x200</div>
<div class="banner" style="left:72px;top:682px;width:630px;height:128px">
  <div class="coins coins-mix" role="img" aria-label="Overlapping copper, silver and gold coins" style="left:360px;width:270px"></div>
  <svg class="shapes" width="390" height="90" viewBox="0 0 390 90">
    <path d="M0 0 H381 L356 55 Q343 84 312 84 H0 Z" fill="var(--brand-blue)"/>
    <path d="M4 4 H374 L352 52 Q340 80 312 80 H4 Z" fill="none" stroke="var(--white)" stroke-width="1.2"/>
  </svg>
  <div class="headline" style="left:16px;top:18px;width:320px">
    <span class="title" style="font-size:24px">Specialty Insurance</span>
    <span class="sub" style="font-size:18px">For your coin collection</span>
  </div>
  <div class="cta" style="left:12px;top:95px;width:97px;height:25px;font-size:9.5px">Learn more</div>
  <div class="presented" style="left:158px;top:109px;font-size:5.5px">Presented by</div>
  <div class="wordmark" style="left:210px;top:98px;font-size:12.5px"><span class="mark" style="width:17px;height:17px"></span>Kestrelby</div>
</div>

<!-- 980x80 -->
<div class="size-label" style="left:72px;top:903px">980x80</div>
<div class="banner" style="left:72px;top:922px;width:630px;height:51px">
  <div class="coins coins-mix" role="img" aria-label="Row of gold, silver and copper coins" style="left:238px;width:220px"></div>
  <svg class="shapes" width="630" height="51" viewBox="0 0 630 51">
    <polygon points="0,0 236,0 243,25.5 236,51 0,51" fill="var(--brand-blue)"/>
    <polygon points="3,3 233,3 239,25.5 233,48 3,48" fill="none" stroke="var(--white)" stroke-width="1"/>
    <polygon points="457,0 630,0 630,51 457,51 450,25.5" fill="var(--white)"/>
    <polygon points="460,3 627,3 627,48 460,48 454,25.5" fill="none" stroke="var(--brand-blue)" stroke-width="1"/>
  </svg>
  <div class="headline" style="left:8px;top:11px;width:220px">
    <span class="title" style="font-size:15.5px">Specialty Insurance</span>
    <span class="sub" style="font-size:11.5px">For your coin collection</span>
  </div>
  <div class="wordmark" style="left:481px;top:14px;font-size:16px"><span class="mark" style="width:22px;height:22px"></span>Kestrelby</div>
</div>

<!-- 500x100 -->
<div class="size-label" style="left:72px;top:996px">500X100</div>
<div class="banner" style="left:72px;top:1016px;width:321px;height:63px">
  <svg class="shapes" width="321" height="63" viewBox="0 0 321 63">
    <rect x="0" y="0" width="200" height="63" fill="var(--brand-blue)"/>
    <rect x="3" y="3" width="190" height="57" fill="none" stroke="var(--white)" stroke-width="1"/>
    <rect x="226" y="3" width="92" height="57" fill="none" stroke="var(--brand-blue)" stroke-width="1"/>
  </svg>
  <div class="coin-round" role="img" aria-label="Polished silver coin" style="left:154px;top:-2px;width:80px;height:67px"></div>
  <div class="headline" style="left:6px;top:20px;width:144px">
    <span class="title" style="font-size:11px">Specialty Insurance</span>
    <span class="sub" style="font-size:8.5px">For your coin collection</span>
  </div>
  <div class="presented" style="left:251px;top:19px;font-size:5.5px">Presented by</div>
  <div class="wordmark" style="left:240px;top:27px;font-size:9px"><span class="mark" style="width:11px;height:11px"></span>Kestrelby</div>
</div>

<!-- 600x30 -->
<div class="size-label" style="left:72px;top:1095px">600X30</div>
<div class="banner" style="left:72px;top:1114px;width:385px;height:19px">
  <div class="coins coins-mix" role="img" aria-label="Row of small gold, silver and copper coins" style="left:234px;width:90px"></div>
  <svg class="shapes" width="385" height="19" viewBox="0 0 385 19">
    <polygon points="0,0 232,0 235,9.5 232,19 0,19" fill="var(--brand-blue)"/>
    <rect x="1.5" y="1.5" width="228" height="16" fill="none" stroke="var(--white)" stroke-width=".7"/>
    <polygon points="326,0 385,0 385,19 326,19 323,9.5" fill="var(--white)"/>
    <rect x="327" y="1.5" width="56.5" height="16" fill="none" stroke="var(--brand-blue)" stroke-width=".7"/>
  </svg>
  <div class="headline" style="left:7px;top:4px;width:230px;text-align:left">
    <span class="title" style="font-size:7.5px;letter-spacing:.4px">Specialty Insurance for your coin collection</span>
  </div>
  <div class="wordmark" style="left:329px;top:5px;font-size:6px;gap:2px"><span class="mark" style="width:7px;height:7px"></span>Kestrelby</div>
</div>

</body>
</html>
```